I am looking for help designing my new business cards. I would like rounded edges and a raised logo on the back of the card. I have 2 Logos. One with a boat in it and one without. I'd like the one on the back to be the one that includes the boat and just the name on the front. I have included multiple formats of my logo. Please let me know if you need anymore.

Target Market(s)

Potential buyers and other sales brokers

Industry/Entity Type

Sales - Yacht / Boat Sales

Contact Information for Business Card

Id liike the front to include just the business name portion of the logo along with my name (Corwin Dalby), phone number (555.318.6027), website address (www.dalbymarineco.example) and not my physical address but just "Kestrel Harbor, ST". The back should include my full logo that has the boat included. This portion I'd prefer raised amd take up the majority of the space there. Thanks!!

Colors
0054AA
0677BA
7BADD7
CADEEF
E8F1F8
0094D4
00A9DD
6FCCEA
C7EBF8
E9F6FB

Requirements
Must have
• Double sided
Nice to have
• My email address: Corwin@dalbymarineco.example The NMTG logo somewhere small on the front of the card
Should not have
• My full address, prefer only "Kestrel Harbor, ST"

```html
<!DOCTYPE html>
<html lang="en">
<head>
<meta charset="utf-8">
<title>Dalby Marine Co – Business Card</title>
<link href="https://fonts.googleapis.com/css2?family=Arimo:wght@400;700&display=swap" rel="stylesheet">
<style>
  :root {
    --backdrop: #e6e6e6;
    --navy: #233872;
    --navy-deep: #1c2e63;
    --brand-blue: #0677BA;
    --brand-dark: #0054AA;
    --sky: #0094D4;
    --ink: #1e1e1e;
    --paper: #f4f4f4;
    --rule: #3a3a3a;
  }
  * { margin: 0; padding: 0; box-sizing: border-box; }
  html, body { width: 1200px; height: 1200px; overflow: hidden; }
  body {
    background: var(--backdrop);
    font-family: "Arimo", Arial, sans-serif;
    position: relative;
  }
  .card {
    position: absolute;
    left: 234px;
    width: 730px;
    height: 418px;
    box-shadow: 0 10px 22px rgba(0,0,0,0.18);
  }
  .card--logo {
    top: 160px;
    background: linear-gradient(135deg, var(--navy), var(--navy-deep));
  }
  .card--contact {
    top: 632px;
    background: linear-gradient(135deg, #e9e9e9, var(--paper) 60%, #f7f7f7);
  }
  .boat-art {
    position: absolute;
    left: 154px;
    top: 54px;
    width: 424px;
    height: 195px;
    border-radius: 6px;
    background: linear-gradient(180deg, rgba(255,255,255,0.10), rgba(0,148,212,0.35));
  }
  .company-name {
    position: absolute;
    left: 0;
    right: 0;
    top: 278px;
    text-align: center;
    color: #ffffff;
    font-weight: 700;
    font-size: 54px;
    letter-spacing: 2px;
    line-height: 1;
  }
  .holder-name {
    position: absolute;
    left: 75px;
    top: 188px;
    color: var(--brand-blue);
    font-weight: 700;
    font-size: 33px;
    letter-spacing: 0.5px;
    line-height: 1;
    white-space: nowrap;
  }
  .divider {
    position: absolute;
    left: 364px;
    top: 162px;
    width: 2px;
    height: 91px;
    background: var(--rule);
  }
  .contact-list {
    position: absolute;
    left: 403px;
    top: 156px;
    list-style: none;
  }
  .contact-item {
    display: flex;
    align-items: center;
    height: 25.5px;
    font-size: 19px;
    color: var(--ink);
    white-space: nowrap;
  }
  .contact-icon {
    width: 14px;
    height: 14px;
    margin-right: 8px;
    fill: var(--brand-dark);
    flex: none;
  }
</style>
</head>
<body>
  <section class="card card--logo">
    <div class="boat-art" role="img" aria-label="Illustration of a center-console fishing boat riding a blue wave"></div>
    <div class="company-name">DALBY MARINE CO</div>
  </section>

  <section class="card card--contact">
    <div class="holder-name">CORWIN DALBY</div>
    <div class="divider"></div>
    <ul class="contact-list">
      <li class="contact-item">
        <svg class="contact-icon" viewBox="0 0 24 24" aria-hidden="true"><path d="M6.6 10.8c1.4 2.8 3.8 5.1 6.6 6.6l2.2-2.2c.3-.3.7-.4 1-.2 1.1.4 2.3.6 3.6.6.6 0 1 .4 1 1V20c0 .6-.4 1-1 1C10.6 21 3 13.4 3 4c0-.6.4-1 1-1h3.5c.6 0 1 .4 1 1 0 1.3.2 2.5.6 3.6.1.3 0 .7-.2 1z"/></svg>
        555.318.6027
      </li>
      <li class="contact-item">
        <svg class="contact-icon" viewBox="0 0 24 24" aria-hidden="true"><path d="M2 5h20v14H2z"/><path d="M3 6l9 7 9-7" fill="none" stroke="#fff" stroke-width="1.6"/></svg>
        corwin@dalbymarineco.example
      </li>
      <li class="contact-item">
        <svg class="contact-icon" viewBox="0 0 24 24" aria-hidden="true"><circle cx="12" cy="12" r="10"/><path d="M2 12h20M12 2c3 3 3 17 0 20M12 2c-3 3-3 17 0 20" fill="none" stroke="#fff" stroke-width="1.5"/></svg>
        www.dalbymarineco.example
      </li>
      <li class="contact-item">
        <svg class="contact-icon" viewBox="0 0 24 24" aria-hidden="true"><path d="M12 1a8 8 0 0 0-8 8c0 6 8 14 8 14s8-8 8-14a8 8 0 0 0-8-8zm0 11a3 3 0 1 1 0-6 3 3 0 0 1 0 6z"/></svg>
        Kestrel Harbor, ST
      </li>
    </ul>
  </section>
</body>
</html>
```